Business Cards for a law firm

Business cards for our law firm. Use our silhoette logo and OAK HARBOR - check our website (www.oakharbor-legal.com)

Contact Information for Business Card

our silhouette logo, OAK HARBOR, 800-555-0147, Dorian Kestrup, dorian@oakharbor-legal.com

Requirements
Must have
• our silhouette logo, OAK HARBOR, 800-555-0147, Dorian Kestrup, dorian@oakharbor-legal.com

```html
<!DOCTYPE html>
<html lang="en">
<head>
<meta charset="utf-8">
<title>Oak Harbor Business Card</title>
<link href="https://fonts.googleapis.com/css2?family=Roboto:wght@400;500;700&display=swap" rel="stylesheet">
<style>
  :root {
    --backdrop: #969696;
    --navy: #23346a;
    --paper: #fafafa;
    --accent: #f5a623;
    --white: #ffffff;
  }
  html, body {
    margin: 0;
    padding: 0;
    width: 1200px;
    height: 1000px;
    overflow: hidden;
    background: var(--backdrop);
    font-family: "Roboto", Arial, sans-serif;
  }
  .canvas {
    position: relative;
    width: 1200px;
    height: 1000px;
  }
  .card {
    position: absolute;
    left: 253px;
    width: 694px;
    height: 400px;
    box-sizing: border-box;
  }
  .card-front {
    top: 61px;
    background: var(--navy);
    display: flex;
    align-items: center;
    justify-content: center;
  }
  .front-mark {
    color: var(--white);
    font-weight: 500;
    font-size: 26px;
    letter-spacing: 3px;
  }
  .card-back {
    top: 523px;
    background: var(--paper);
    color: var(--navy);
  }
  .brand {
    position: absolute;
    left: 47px;
    top: 62px;
    display: flex;
    align-items: center;
    gap: 14px;
  }
  .brand-square {
    width: 26px;
    height: 26px;
    background: var(--navy);
  }
  .brand-name {
    font-weight: 500;
    font-size: 34px;
    letter-spacing: 2px;
    color: var(--navy);
  }
  .person-name {
    position: absolute;
    left: 46px;
    top: 265px;
    margin: 0;
    font-weight: 700;
    font-size: 23px;
  }
  .name-rule {
    position: absolute;
    left: 47px;
    top: 305px;
    width: 103px;
    height: 3px;
    background: var(--accent);
  }
  .contact {
    position: absolute;
    left: 47px;
    top: 318px;
    font-size: 18px;
    line-height: 22px;
  }
  .website {
    position: absolute;
    right: 37px;
    top: 340px;
    font-size: 18px;
    line-height: 22px;
  }
  .website strong { font-weight: 700; }
</style>
</head>
<body>
<div class="canvas">
  <section class="card card-front">
    <span class="front-mark">OAK HARBOR</span>
  </section>

  <section class="card card-back">
    <div class="brand">
      <span class="brand-square"></span>
      <span class="brand-name">OAK HARBOR</span>
    </div>
    <h1 class="person-name">Dorian Kestrup</h1>
    <div class="name-rule"></div>
    <div class="contact">
      dorian@oakharbor-legal.com<br>
      (800) 555-0147
    </div>
    <div class="website"><strong>oakharbor-legal</strong>.com</div>
  </section>
</div>
</body>
</html>
```